Information Technology Company needs a Website...

We need a single page website for new technology company called:

MERIDEL FALLS TECHNOLOGY GROUP
Based in Ojai CA.

We are offering three primary services:

- Business Solutions

- IT Services

- Software Implementation and Consulting

We want a single page design where all content scrolls down/up on one page. We're looking for the following characteristics:

- Home/Landing
- Active background with panoramic view (Will provide content)

- Business Solutions, IT Services, Software Implementation and Consulting

List of software vendors we recommend (Company logos)

- About
- History
- Our Team
- Partners

I'll upload our new logo as soon as we get the design files. I'll also send over some example website layout's that we like shortly.

Target Market(s)

Small/Medium Businesses

Industry/Entity Type

Information Technology

Number of Pages Required

1 page

Font styles to use
Other font styles liked:
• Sansation

Requirements
Must have
• Full page browser width, easy navigation and visibility. Creative design, not like every other "Technology" website template. Should be the "One Page" design where each section is below the next and the user scrolls down the page through the whole site. I like the concept of the following website in the main "Whiteboard" image:
• http://www.plavorix.com/design/4829137
• And the way this site does the active panoramic background:
• http://www.kelbrantworks.com/
• Something interesting and appealing to potential clients looking for Small/Medium business solutions and IT Services.
• Use uploaded Logo to establish color and theme for website.
Should not have
• Look the same as every other information technology website template.

```html
<!DOCTYPE html>
<html lang="en">
<head>
<meta charset="utf-8">
<title>Meridel Falls Technology Group</title>
<link href="https://fonts.googleapis.com/css2?family=Play:wght@400;700&family=Raleway:wght@300;400&display=swap" rel="stylesheet">
<style>
  :root {
    --orange: #ec4e03;
    --sky: #4a6fd8;
    --sky-deep: #3350b8;
    --link-blue: #3e6ad6;
    --ink: #1a1a1a;
    --text: #333333;
    --nav-grey: #6b6b6b;
    --white: #ffffff;
    --slate-top: #4a5a80;
    --slate-bottom: #1e2a4e;
  }
  * { box-sizing: border-box; margin: 0; padding: 0; }
  html, body { width: 1040px; height: 1200px; overflow: hidden; background: var(--white); }
  body { position: relative; font-family: "Play", sans-serif; color: var(--text); }

  .site-header { position: absolute; left: 0; top: 0; width: 1040px; height: 78px; background: var(--white); border-bottom: 2px solid var(--orange); }
  .brand { position: absolute; left: 130px; top: 20px; display: flex; align-items: center; gap: 8px; }
  .brand-mark { width: 12px; height: 12px; background: var(--orange); }
  .brand-name { font-family: "Play", sans-serif; font-weight: 700; font-size: 13px; line-height: 15px; color: #3a3a3a; letter-spacing: 0.5px; width: 150px; }

  .main-nav { position: absolute; top: 22px; right: 142px; display: flex; align-items: center; height: 33px; }
  .main-nav a { font-family: "Raleway", sans-serif; font-weight: 300; font-size: 16px; color: var(--nav-grey); text-decoration: none; margin-left: 27px; position: relative; }
  .main-nav a.is-active { color: var(--orange); font-family: "Play", sans-serif; font-weight: 400; }
  .main-nav a.is-active::after { content: ""; position: absolute; left: 0; right: 0; bottom: -10px; height: 2px; background: var(--orange); }
  .main-nav a.nav-contact { background: var(--orange); color: var(--white); font-family: "Play", sans-serif; font-weight: 700; padding: 7px 11px; margin-left: 12px; }

  .hero-band { position: absolute; left: 0; top: 80px; width: 1040px; height: 594px; background: linear-gradient(180deg, var(--sky) 0%, var(--sky) 45%, #3d5cc4 70%, var(--sky-deep) 100%); }
  .hero-frame { position: absolute; left: 130px; top: 186px; width: 768px; height: 488px; background: var(--white); }
  .hero-board { position: absolute; left: 138px; top: 194px; width: 752px; height: 480px; background: linear-gradient(160deg, var(--slate-top) 0%, #34426a 55%, var(--slate-bottom) 100%); overflow: hidden; }
  .hero-title { position: absolute; left: 398px; top: 68px; font-family: "Play", sans-serif; font-weight: 700; font-size: 42px; line-height: 48px; color: var(--white); white-space: nowrap; }
  .hero-tagline { position: absolute; left: 398px; top: 119px; font-family: "Play", sans-serif; font-size: 26px; color: var(--white); white-space: nowrap; }
  .hero-pill { position: absolute; left: 528px; top: 166px; }
  .hero-copy { position: absolute; left: 398px; top: 280px; width: 320px; font-size: 13.6px; line-height: 17.2px; color: var(--white); }

  .solutions-banner { position: absolute; left: 129px; top: 706px; width: 770px; height: 72px; border: 1px solid #d4d4d4; background: var(--white); box-shadow: 0 14px 14px -10px rgba(0,0,0,0.35); }
  .solutions-banner-inner { position: absolute; left: 8px; top: 8px; right: 8px; bottom: 8px; background: var(--orange); color: var(--white); text-align: center; padding-top: 10px; }
  .solutions-title { font-weight: 700; font-size: 18px; line-height: 18px; }
  .solutions-sub { font-style: italic; font-size: 16px; line-height: 18px; }

  .service { position: absolute; width: 140px; text-align: center; font-size: 14.4px; line-height: 18.5px; color: var(--ink); }
  .service .icon { display: block; margin: 0 auto 10px; }
  .service em { font-style: normal; color: var(--link-blue); }
  .service.is-highlighted { background: var(--orange); color: var(--white); width: 134px; height: 192px; padding-top: 24px; }
  .service.is-highlighted em { color: var(--white); }
  .learn-more { display: inline-block; margin-top: 12px; border: 1px solid var(--white); color: var(--white); font-size: 10px; font-weight: 700; padding: 6px 14px; text-decoration: none; }
</style>
</head>
<body>

<header class="site-header">
  <div class="brand"><span class="brand-mark"></span><span class="brand-name">MERIDEL FALLS TECHNOLOGY GROUP</span></div>
  <nav class="main-nav">
    <a href="#home">Home</a>
    <a href="#about" class="is-active">About</a>
    <a href="#history">History</a>
    <a href="#team">Our Team</a>
    <a href="#partners">Partners</a>
    <a href="#contact" class="nav-contact">Contact Us</a>
  </nav>
</header>

<section class="hero-band" role="img" aria-label="Panoramic photograph of blue mountain ridges"></section>
<div class="hero-frame"></div>
<section class="hero-board">
  <div role="img" aria-label="Chalkboard illustration of cloud computing, VoIP and virtualization sketches with a large white cloud" style="position:absolute;inset:0;"></div>
  <h1 class="hero-title">MERIDEL FALLS</h1>
  <p class="hero-tagline">your technological partner</p>
  <svg class="hero-pill" width="32" height="94" viewBox="0 0 32 94" aria-hidden="true">
    <circle cx="16" cy="16" r="15" fill="#fff"/>
    <circle cx="16" cy="78" r="15" fill="#fff"/>
    <rect x="9" y="16" width="14" height="62" fill="#fff"/>
  </svg>
  <p class="hero-copy">Meridel Falls technology group&nbsp; is a boutique market research firm known for our hands-on, service-oriented approach. We attract “corpo­rate revolutionaries” within Global 1,000 com­panies who are seeking to forge new paths, new products and new services.</p>
</section>

<section class="solutions-banner">
  <div class="solutions-banner-inner">
    <div class="solutions-title">BUSINESS SOLUTIONS</div>
    <div class="solutions-sub">for small &amp; medium businesses</div>
  </div>
</section>

<div class="service" style="left:174px;top:852px;">
  <svg class="icon" width="64" height="56" viewBox="0 0 64 56" aria-hidden="true"><path d="M14 48 C4 48 0 40 2 34 C4 27 10 25 14 26 C15 16 22 10 31 10 C40 10 46 16 48 24 C56 23 62 29 62 36 C62 43 56 48 50 48 Z" fill="#3e6ad6"/></svg>
  Cloud <em>Computing</em>
</div>
<div class="service" style="left:314px;top:850px;">
  <svg class="icon" width="56" height="58" viewBox="0 0 56 58" aria-hidden="true"><circle cx="28" cy="29" r="26" fill="none" stroke="#111" stroke-width="3"/><path d="M19 17 C16 19 15 23 17 28 C20 35 25 40 32 43 C36 44 39 43 41 40 L36 35 L32 38 C28 36 24 32 22 28 L25 24 Z" fill="#111"/></svg>
  Voip <em>Solutions</em>
</div>
<div class="service" style="left:450px;top:852px;">
  <svg class="icon" width="48" height="56" viewBox="0 0 48 56" aria-hidden="true"><path d="M6 44 V4 H34" fill="none" stroke="#111" stroke-width="4"/><rect x="14" y="12" width="28" height="40" fill="none" stroke="#111" stroke-width="4"/></svg>
  <em>Virtualization</em>
</div>
<div class="service" style="left:588px;top:852px;">
  <svg class="icon" width="56" height="56" viewBox="0 0 56 56" aria-hidden="true"><ellipse cx="22" cy="9" rx="20" ry="7" fill="#111"/><path d="M2 14 C2 22 42 22 42 14 V22 C42 30 2 30 2 22 Z M2 28 C2 36 42 36 42 28 V36 C42 44 2 44 2 36 Z" fill="#111"/><path d="M36 36 H56 M46 26 V48" stroke="#111" stroke-width="6"/></svg>
  Disaster <em>Recovery</em>
</div>
<div class="service" style="left:727px;top:850px;">
  <svg class="icon" width="56" height="58" viewBox="0 0 56 58" aria-hidden="true"><path d="M6 30 V14 C6 6 12 2 16 2 C20 2 26 6 26 14 V22" fill="none" stroke="#111" stroke-width="5"/><rect x="16" y="26" width="38" height="30" rx="3" fill="#111"/><circle cx="35" cy="38" r="3" fill="#fff"/><rect x="34" y="38" width="2" height="8" fill="#fff"/></svg>
  Open <em>Source Software</em>
</div>

<div class="service" style="left:174px;top:1026px;">
  <svg class="icon" width="64" height="56" viewBox="0 0 64 56" aria-hidden="true"><rect x="3" y="3" width="58" height="40" fill="none" stroke="#111" stroke-width="5"/><rect x="26" y="43" width="12" height="8" fill="#111"/><rect x="18" y="50" width="28" height="5" fill="#111"/></svg>
  Remote <em>Desktop Applications</em>
</div>
<div class="service" style="left:314px;top:1028px;">
  <svg class="icon" width="54" height="54" viewBox="0 0 54 54" aria-hidden="true"><rect x="0" y="0" width="54" height="54" fill="#111"/><rect x="8" y="7" width="38" height="9" fill="#fff"/><g fill="#fff"><circle cx="13" cy="25" r="3"/><circle cx="22" cy="25" r="3"/><circle cx="31" cy="25" r="3"/><circle cx="40" cy="25" r="3"/><circle cx="13" cy="34" r="3"/><circle cx="22" cy="34" r="3"/><circle cx="31" cy="34" r="3"/><circle cx="40" cy="34" r="3"/><circle cx="13" cy="43" r="3"/><circle cx="22" cy="43" r="3"/><circle cx="31" cy="43" r="3"/><circle cx="40" cy="43" r="3"/></g></svg>
  Enterprise <em>Resource Planning</em> (ERP) Accounting
</div>
<div class="service" style="left:460px;top:1027px;width:130px;">
  <svg class="icon" width="56" height="56" viewBox="0 0 56 56" aria-hidden="true"><circle cx="28" cy="28" r="28" fill="#111"/><text x="28" y="40" text-anchor="middle" font-family="Play, sans-serif" font-weight="700" font-size="34" fill="#fff">?</text></svg>
  Applications for<br><em>Help Desk</em>
</div>
<div class="service is-highlighted" style="left:592px;top:1002px;">
  <svg class="icon" width="46" height="56" viewBox="0 0 46 56" aria-hidden="true"><circle cx="23" cy="14" r="14" fill="#fff"/><path d="M0 56 V46 C0 36 10 30 23 30 C36 30 46 36 46 46 V56 Z" fill="#fff"/></svg>
  Customer Relationship Management
  <a href="#crm" class="learn-more">LEARN MORE</a>
</div>
<div class="service" style="left:727px;top:1030px;">
  <svg class="icon" width="58" height="54" viewBox="0 0 58 54" aria-hidden="true"><g fill="#111"><circle cx="29" cy="8" r="8"/><circle cx="12" cy="14" r="7"/><circle cx="46" cy="14" r="7"/><path d="M0 54 V34 C0 26 6 22 12 22 C18 22 24 26 24 34 V54 Z"/><path d="M34 54 V34 C34 26 40 22 46 22 C52 22 58 26 58 34 V54 Z"/><path d="M14 54 V32 C14 22 20 18 29 18 C38 18 44 22 44 32 V54 Z"/></g><circle cx="29" cy="38" r="6" fill="#fff"/></svg>
  Teleconference <em>Services</em>
</div>

</body>
</html>
```